Local Horticulturalist needs Business card design

Meridel Horticulture would like to update our existing business card and utilize our new logo (design attached)....we specialize in getting the best out of our customers yard with professional maintenance programs, expert pruning and hedging and garden restorations.
Utilizing colors from attached logo I would like a design that implies professionalism and if possible our businesses love of restoration through plants.
I also sometimes write down for my customers a start date and price on the back of my current card
Target Market(s)
Home owners
Contractors
Industry/Entity Type
Gardener
Contact Information for Business Card
Gareth Volkstrom | Horticulturalist
ph: 0438275946
meridelhort@fernmail.example
www.meridelhorticulture.example.au
Requirements
Must have
- crucial information easy to read
- incorporate current logo
- Horticulturalist listed preferably near name
Nice to have
- currently I write a job start date and price on the back of my current card so something that integrates this would be beneficial
Should not have
- be pretty or flowerey
- be too white or basic

```html
<!DOCTYPE html>
<html lang="en">
<head>
<meta charset="utf-8">
<title>Meridel Horticulture – Business Card</title>
<link rel="stylesheet" href="https://fonts.googleapis.com/css2?family=Alegreya:wght@400;500&family=Alegreya+Sans:wght@700&display=swap">
<style>
  :root {
    --page-bg: #eef8cf;
    --page-glow: #fbfde9;
    --band-dark: #8a9e34;
    --band-light: #c4d867;
    --panel-light: #eef8c4;
    --panel-white: #fdfef4;
    --ink-brown: #7a6a5c;
    --ink-white: #ffffff;
    --brand-green: #7fb52a;
  }
  * { margin: 0; padding: 0; box-sizing: border-box; }
  html, body { width: 1200px; height: 1000px; overflow: hidden; }
  body {
    background: radial-gradient(ellipse at 50% 55%, var(--page-glow) 0%, var(--page-bg) 70%);
    font-family: "Alegreya", Georgia, serif;
    position: relative;
  }
  .card {
    position: absolute;
    overflow: hidden;
    box-shadow: 0 8px 22px rgba(90, 110, 40, 0.28);
  }
  .band { position: absolute; left: 0; width: 100%; }
  .band--green { background: linear-gradient(100deg, var(--band-dark) 0%, var(--band-light) 55%, var(--band-dark) 100%); }
  .band--light { background: linear-gradient(100deg, var(--panel-light) 0%, var(--panel-white) 55%, var(--panel-light) 100%); }

  .brand { position: absolute; display: flex; align-items: center; }
  .brand__dot { border-radius: 50%; background: var(--brand-green); flex: none; }
  .brand__name {
    font-family: "Alegreya Sans", Arial, sans-serif;
    font-weight: 700;
    color: var(--brand-green);
    white-space: nowrap;
  }

  /* Front */
  .card--front { left: 100px; top: 100px; width: 683px; height: 365px; }
  .card--front .brand { left: 60px; top: 30px; }
  .card--front .brand__dot { width: 82px; height: 82px; margin-right: 12px; }
  .card--front .brand__name { font-size: 40px; }
  .person { position: absolute; left: 0; width: 100%; text-align: center; color: var(--ink-white); }
  .person__name {
    position: absolute; left: 178px; width: 342px; top: 162px;
    font-size: 33px; line-height: 1; padding-bottom: 5px;
    border-bottom: 2px solid var(--ink-white);
  }
  .person__role { position: absolute; left: 0; width: 100%; top: 206px; font-size: 22px; }
  .contact { position: absolute; left: 0; width: 100%; top: 282px; text-align: center; color: var(--ink-brown); font-size: 15px; font-weight: 500; }
  .contact__line { display: flex; justify-content: center; align-items: center; gap: 7px; height: 23px; }
  .contact__icon { width: 13px; height: 13px; fill: var(--ink-brown); }

  /* Back */
  .card--back { left: 433px; top: 560px; width: 684px; height: 367px; }
  .card--back .brand { left: 172px; top: 51px; }
  .card--back .brand__dot { width: 52px; height: 52px; margin-right: 9px; }
  .card--back .brand__name { font-size: 25px; }
  .services { position: absolute; left: 0; width: 100%; top: 131px; text-align: center; color: var(--ink-white); font-size: 18.5px; line-height: 25.4px; }
  .job-notes { position: absolute; right: 342px; top: 274px; text-align: right; color: var(--ink-brown); font-size: 20px; line-height: 23px; }
</style>
</head>
<body>

<section class="card card--front" aria-label="Business card front">
  <div class="band band--light" style="top:0;height:128px"></div>
  <div class="band band--green" style="top:128px;height:135px"></div>
  <div class="band band--light" style="top:263px;height:102px"></div>

  <div class="brand">
    <span class="brand__dot"></span>
    <span class="brand__name">Meridel Horticulture</span>
  </div>

  <div class="person">
    <p class="person__name">Gareth Volkstrom</p>
    <p class="person__role">Horticulturalist</p>
  </div>

  <div class="contact">
    <p class="contact__line">
      <svg class="contact__icon" viewBox="0 0 24 24" aria-hidden="true"><path d="M6.6 10.8a15 15 0 0 0 6.6 6.6l2.2-2.2c.3-.3.7-.4 1-.2 1.1.4 2.3.6 3.6.6.6 0 1 .4 1 1V20c0 .6-.4 1-1 1A17 17 0 0 1 3 4c0-.6.4-1 1-1h3.5c.6 0 1 .4 1 1 0 1.3.2 2.5.6 3.6.1.3 0 .7-.2 1z"/></svg>
      043-827-5946
    </p>
    <p class="contact__line">
      <svg class="contact__icon" viewBox="0 0 24 24" aria-hidden="true"><path d="M2 5h20v14H2z M2 5l10 7 10-7" fill="none" stroke="#7a6a5c" stroke-width="0"/><path d="M2 6l10 6.5L22 6v13H2z"/><path d="M2 5h20l-10 6.3z"/></svg>
      meridelhort@fernmail.example
    </p>
    <p class="contact__line">
      <svg class="contact__icon" viewBox="0 0 24 24" aria-hidden="true"><g fill="none" stroke="#7a6a5c" stroke-width="2"><circle cx="12" cy="12" r="10"/><ellipse cx="12" cy="12" rx="4.5" ry="10"/><path d="M2 12h20M4 7h16M4 17h16"/></g></svg>
      www.meridelhorticulture.example.au
    </p>
  </div>
</section>

<section class="card card--back" aria-label="Business card back">
  <div class="band band--green" style="top:0;height:37px"></div>
  <div class="band band--light" style="top:37px;height:91px"></div>
  <div class="band band--green" style="top:128px;height:135px"></div>
  <div class="band band--light" style="top:263px;height:62px"></div>
  <div class="band band--green" style="top:325px;height:42px"></div>

  <div class="brand">
    <span class="brand__dot"></span>
    <span class="brand__name">Meridel Horticulture</span>
  </div>

  <div class="services">
    <p>Restore your garden to its former glory</p>
    <p>Design and cultivate your new garden or landscape</p>
    <p>Make your garden more water friendly with drip irrigation</p>
    <p>Keep your indoor plants alive and thriving</p>
    <p>Grow a productive home fruit and vegie garden</p>
  </div>

  <div class="job-notes">
    <p>Start Date:</p>
    <p>Price:</p>
  </div>
</section>

</body>
</html>
```